Pop Up Banner Design (30x72in) for events for Meridian Tongue Institute

30 x 72 inch design for a pop up banner or 2 (or 3) to advertise my business, Meridian Tongue Institute, featuring www.meridiantongueinst.com

This banner will be used at anime conventions, or local events to promote the business to the general public, schools, or asian culture lovers.

Color scheme to identify with the logo that is attached. Imagery would be great!

Target audience: teens to 30s
Benefits MTI Offers: learning japanese language, learning japanese culture, peer study groups and events, one-on-one or classroom setting, in person or virtual learning, Standard Lexical Aptitude Exam (SLAE) preparation, homework, guided tours to Japan once a year, translation services, conversation tables, etc.

Target Market(s)

teens to 30 year olds

Industry/Entity Type

Education

Font styles to use
Sans Serif

Colors
ec1f27
ffffff
000000

Requirements
Must have
• logo, imagery, benefits strategically explained, website

```html
<!DOCTYPE html>
<html lang="en">
<head>
<meta charset="utf-8">
<title>Meridian Tongue Institute – Event Banner</title>
<link rel="stylesheet" href="https://fonts.googleapis.com/css2?family=Open+Sans:wght@400;600;700&family=Noto+Serif:wght@400&display=swap">
<style>
  :root {
    --brand-red: #d0202a;
    --ink: #1f1f1f;
    --paper: #ffffff;
    --sky: #c3ccd3;
    --foliage: #b8452e;
    --pine: #4e6a3c;
    --lake: #2f6596;
  }
  html, body {
    margin: 0;
    padding: 0;
    width: 1200px;
    height: 2880px;
    overflow: hidden;
    background: var(--paper);
  }
  .banner {
    position: relative;
    width: 1200px;
    height: 2880px;
    background: var(--brand-red);
    overflow: hidden;
    font-family: "Open Sans", Arial, sans-serif;
    color: var(--paper);
  }
  .edge-bar {
    position: absolute;
    left: 0;
    width: 1200px;
    background: var(--ink);
  }
  .edge-bar--top { top: 0; height: 24px; }
  .edge-bar--bottom { bottom: 0; height: 32px; }

  .brand {
    position: absolute;
    top: 100px;
    left: 0;
    width: 1200px;
    text-align: center;
  }
  .brand__mark {
    display: block;
    width: 260px;
    height: 260px;
    margin: 0 auto;
    border-radius: 50%;
    background: var(--paper);
  }
  .brand__name {
    margin: 58px 0 0;
    font-size: 40px;
    line-height: 50px;
    font-weight: 400;
    letter-spacing: 2px;
    text-transform: uppercase;
  }
  .brand-rule {
    position: absolute;
    top: 514px;
    left: 0;
    width: 1200px;
    height: 8px;
    background: var(--paper);
  }

  .benefits {
    position: absolute;
    top: 570px;
    left: 190px;
    width: 800px;
  }
  .benefits__title {
    margin: 0 0 22px;
    font-size: 44px;
    font-weight: 700;
  }
  .benefits__list {
    list-style: none;
    margin: 0;
    padding: 0;
    font-family: "Noto Serif", Georgia, serif;
    font-size: 41px;
    line-height: 84px;
  }
  .benefits__list li {
    position: relative;
    padding-left: 48px;
  }
  .benefits__list li::before {
    content: "";
    position: absolute;
    left: 0;
    top: 34px;
    width: 16px;
    height: 16px;
    border-radius: 50%;
    background: var(--paper);
  }

  .scenery {
    position: absolute;
    top: 1150px;
    left: 0;
    width: 1200px;
    height: 1250px;
    display: block;
  }

  .cta {
    position: absolute;
    top: 2400px;
    left: 0;
    width: 1200px;
    height: 320px;
    background: var(--ink);
    text-align: center;
    box-sizing: border-box;
    padding-top: 40px;
  }
  .cta p { margin: 0; }
  .cta__lead { font-size: 52px; line-height: 76px; }
  .cta__url { font-size: 64px; line-height: 84px; font-weight: 600; }
  .cta__tail { font-size: 52px; line-height: 76px; }
</style>
</head>
<body>
<main class="banner">
  <div class="edge-bar edge-bar--top"></div>

  <header class="brand">
    <span class="brand__mark" aria-hidden="true"></span>
    <h1 class="brand__name">Meridian Tongue Institute</h1>
  </header>
  <div class="brand-rule"></div>

  <section class="benefits">
    <h2 class="benefits__title">MTI Can Help You:</h2>
    <ul class="benefits__list">
      <li>Learn Japanese</li>
      <li>Virtually or In Person*</li>
      <li>One on One or Classroom setting</li>
      <li>Experience Japanese Culture</li>
      <li>Prep for the SLAE</li>
      <li>Connect with other learners</li>
      <li>One on one homework correction</li>
      <li>Practice speaking with virtual conversation tables and more!</li>
    </ul>
  </section>

  <svg class="scenery" viewBox="0 0 1200 1250" xmlns="http://www.w3.org/2000/svg">
    <defs>
      <linearGradient id="sceneTones" x1="0" y1="0" x2="0" y2="1">
        <stop offset="0" stop-color="var(--sky)"/>
        <stop offset="0.35" stop-color="var(--foliage)"/>
        <stop offset="0.55" stop-color="var(--pine)"/>
        <stop offset="0.75" stop-color="var(--lake)"/>
        <stop offset="1" stop-color="#24527c"/>
      </linearGradient>
    </defs>
    <path class="scenery__swoosh" fill="#1f1f1f"
          d="M1200,0 C1000,250 700,210 420,370 C260,460 110,520 0,560 L0,650 C200,570 400,480 620,420 C860,355 1050,320 1200,300 Z"/>
    <path class="scenery__highlight" fill="#ffffff"
          d="M0,650 C200,570 400,480 620,420 C860,355 1050,320 1200,300 L1200,340 C1050,360 860,395 640,455 C420,515 200,600 0,690 Z"/>
    <path class="scenery__photo" fill="url(#sceneTones)" role="img"
          aria-label="Golden pavilion temple beside a still lake, framed by red autumn maple leaves and pine trees"
          d="M0,690 C200,600 420,515 640,455 C860,395 1050,360 1200,340 L1200,1250 L0,1250 Z"/>
  </svg>

  <footer class="cta">
    <p class="cta__lead">Check out</p>
    <p class="cta__url">www.meridiantongueinst.com</p>
    <p class="cta__tail">for more details</p>
  </footer>

  <div class="edge-bar edge-bar--bottom"></div>
</main>
</body>
</html>
```